"Quillfen" Paint Tools

Design logo and packaging for a range of paint tools. We need a bullseye style logo. Packaging background colour Pantone 425c. Main colours to be 2423c and 3015c. Attached is examples of another brand in our range for reference and for what we need the packaging to be on. Refer to attachments. We need designs in the di cuts for "50mm Wall Brush", "63mm Wall Brush, "75mm Wall Brush", "50mm Sash Cutter", "63mm Sash Cutter".

Requirements
Must have
• Quillfen Painting Tools

The Quillfen Brush range have been designed to give you the perfect finish for your painting project.

The brushes are made from the finest materials using the best craftsman.

The Quillfen Brushes use the latest filament technology to ensure that the brushes meet the performance demands of the professional painter. Our unique blend of high performance filament gives you the perfect balance between paint pick up, brush control, paint release and a smooth professional finish.

We provide a 100% quality guarantee

Made in China

```html
<!DOCTYPE html>
<html lang="en">
<head>
<meta charset="utf-8">
<title>Quillfen Paint Tools – Logo &amp; Wall Brush Packaging</title>
<link rel="stylesheet" href="https://fonts.googleapis.com/css2?family=Inter:wght@400;700;800&family=Archivo+Black&display=swap">
<style>
  :root {
    --stage: #000000;
    --brand-blue: #0063a0;
    --pack-grey: #3d3d3e;
    --brand-green: #00a82d;
    --white: #ffffff;
  }
  html, body {
    margin: 0;
    padding: 0;
    width: 1200px;
    height: 859px;
    overflow: hidden;
    background: var(--stage);
  }
  .artboard { display: block; width: 1200px; height: 859px; }
  .sans { font-family: "Inter", Arial, sans-serif; }
  .wordmark { font-family: "Inter", Arial, sans-serif; font-weight: 700; fill: var(--white); }
  .product-title { font-family: "Archivo Black", "Arial Black", sans-serif; fill: var(--brand-green); }
  .green-label { font-family: "Inter", Arial, sans-serif; font-weight: 700; fill: var(--brand-green); }
  .body-copy { font-family: "Inter", Arial, sans-serif; font-weight: 400; fill: var(--white); }
  .size-label { font-family: "Inter", Arial, sans-serif; font-weight: 800; fill: var(--brand-green); }
</style>
</head>
<body>
<svg class="artboard" viewBox="0 0 1258 901" xmlns="http://www.w3.org/2000/svg">
  <rect class="stage" width="1258" height="901" fill="var(--stage)"/>

  <!-- Brand mark -->
  <g class="brand-lockup">
    <circle class="brand-dot" cx="400" cy="385" r="108" fill="var(--brand-blue)"/>
    <text class="wordmark" x="400" y="600" font-size="114" text-anchor="middle" letter-spacing="-2">Quillfen</text>
  </g>

  <!-- Die-cut packaging -->
  <g class="packaging">
    <!-- hang tab -->
    <path class="hang-tab" fill="var(--brand-blue)"
      d="M920 112 L955 86 L1015 86 L1050 112 L1050 220 L920 220 Z"/>
    <path class="hang-hole" fill="var(--stage)"
      d="M965 165 Q965 158 972 158 L998 158 Q1005 158 1005 165 L1005 205 Q1005 212 998 212 L992 212 Q985 196 978 212 L972 212 Q965 212 965 205 Z"/>

    <!-- side flaps -->
    <path class="flap flap-left" fill="var(--pack-grey)"
      d="M798 222 L900 216 L888 518 L884 518 Q825 420 787 250 Q785 226 798 222 Z"/>
    <path class="flap flap-right" fill="var(--pack-grey)"
      d="M1172 222 L1080 216 L1094 518 L1100 520 Q1160 430 1186 250 Q1188 226 1172 222 Z"/>

    <!-- blue front band -->
    <path class="front-band" fill="var(--brand-blue)"
      d="M878 215 L1093 215 L1062 520 L906 520 Z"/>

    <!-- front panel -->
    <g class="front-panel">
      <rect x="930" y="225" width="111" height="276" fill="var(--pack-grey)"/>
      <circle cx="985" cy="260" r="17" fill="var(--brand-blue)"/>
      <text class="wordmark" x="985" y="300" font-size="19" text-anchor="middle">Quillfen</text>
      <text class="product-title" x="985" y="376" font-size="31" text-anchor="middle">WALL</text>
      <text class="product-title" x="985" y="406" font-size="31" text-anchor="middle">BRUSH</text>
      <text class="green-label" x="946" y="434" font-size="6" letter-spacing="1.4">FOR ALL PAINT TYPES</text>
      <text class="body-copy" x="946" y="445" font-size="7.2">Superior paint pick up, release,</text>
      <text class="body-copy" x="946" y="455" font-size="7.2">control &amp; smooth finish</text>
      <text class="size-label" x="985" y="485" font-size="11" text-anchor="middle">2 INCH | 50MM</text>
    </g>

    <!-- care instructions on right flap -->
    <g class="care-copy" transform="rotate(7 1100 290)">
      <text class="green-label" x="1100" y="292" font-size="6.3">BRUSH CLEANING</text>
      <text class="green-label" x="1100" y="300" font-size="6.3">&amp; STORAGE</text>
      <text class="body-copy" font-size="6">
        <tspan x="1098" y="318">Clean your brush</tspan>
        <tspan x="1098" y="326">immediately after use.</tspan>
        <tspan x="1098" y="338">Don't allow paint to dry</tspan>
        <tspan x="1098" y="346">on brush.</tspan>
        <tspan x="1098" y="358">If using water based paints,</tspan>
        <tspan x="1098" y="366">wash in warm soapy water.</tspan>
        <tspan x="1098" y="378">If using oil based paints,</tspan>
        <tspan x="1098" y="386">first wash with solvent</tspan>
        <tspan x="1098" y="394">cleaner or mineral spirits</tspan>
        <tspan x="1098" y="402">and then warm soapy water.</tspan>
        <tspan x="1098" y="414">Rinse brush thoroughly,</tspan>
        <tspan x="1098" y="422">shake out excess water,</tspan>
        <tspan x="1098" y="430">then comb bristles straight</tspan>
        <tspan x="1098" y="438">and allow to dry.</tspan>
        <tspan x="1098" y="450">Never soak the brush.</tspan>
        <tspan x="1098" y="462">Hang brush with filament</tspan>
        <tspan x="1098" y="470">pointing down.</tspan>
      </text>
    </g>

    <!-- back panel -->
    <path class="back-panel" fill="var(--pack-grey)"
      d="M920 520 L1052 520 L1052 798 Q1052 812 1038 812 L934 812 Q920 812 920 798 Z"/>
    <g class="back-copy" transform="rotate(180 986 665)">
      <circle cx="986" cy="548" r="16" fill="var(--brand-blue)"/>
      <text class="wordmark" x="932" y="588" font-size="19">Quillfen</text>
      <text class="body-copy" font-size="5.6">
        <tspan x="932" y="606">With years of brush making experience,</tspan>
        <tspan x="932" y="613">we have developed a superior paint</tspan>
        <tspan x="932" y="620">brush to make your painting job easier.</tspan>
        <tspan x="932" y="627">Formulated with our own unique blend</tspan>
        <tspan x="932" y="634">of synthetic filament technology, the</tspan>
        <tspan x="932" y="641">Quillfen Wall Brush gives you the</tspan>
        <tspan x="932" y="648">perfect balance of paint pick up and</tspan>
        <tspan x="932" y="655">release, brush control and a superior</tspan>
        <tspan x="932" y="662">smooth finish.</tspan>
        <tspan x="932" y="672">Ideal for all interior wall &amp; timber</tspan>
        <tspan x="932" y="679">painting applications.</tspan>
      </text>
      <text class="green-label" x="932" y="692" font-size="5.8" letter-spacing="0.6">QUALITY GUARANTEE</text>
      <text class="body-copy" font-size="5.6">
        <tspan x="932" y="706">Harlow Products</tspan>
        <tspan x="932" y="713">18 Kestrel Rd,</tspan>
        <tspan x="932" y="720">ALDER BAY 2290</tspan>
        <tspan x="932" y="727">NSW AUSTRALIA</tspan>
        <tspan x="932" y="738">Code: 17348</tspan>
        <tspan x="932" y="749">Made in China</tspan>
      </text>
    </g>
  </g>
</svg>
</body>
</html>
```